Super elegant, crisp & clean Business card design required

We recently upgraded our branding - which is on our website - tavolenstudio.com

I would like a simple, yet elegant, clean business card design please.

The font of my logo is Cinzel - and because of the natural colour - it's best to have this on a black background.

I would like to have the back of the business card - with simply my logo.

PLEASE DO NOT SUBMIT A COMPLICATED / UNCLEAN DESIGN

Industry/Entity Type

Business

Contact Information for Business Card

Danvir Okelowa Photography

Font styles to use
Other font styles liked:
• Cinzel

Requirements
Must have
• A backpage with nothing but my logo
• Simple design - stands out
Should not have
• Colour that dont align with my logo
• Over complicated '/ non symmetrical design

```html
<!DOCTYPE html>
<html lang="en">
<head>
<meta charset="UTF-8">
<title>Danvir Okelowa Photography — Business Card</title>
<link rel="stylesheet" href="https://fonts.googleapis.com/css2?family=Cinzel:wght@400;500&family=Questrial&display=swap">
<style>
  :root {
    --page-bg: #d8cfc4;
    --card-frost: #ebe7e0;
    --panel-black: #000000;
    --accent-taupe: #827763;
    --text-gold: #a39478;
    --logo-taupe: #7d7464;
  }
  * { margin: 0; padding: 0; box-sizing: border-box; }
  html, body {
    width: 1200px;
    height: 902px;
    overflow: hidden;
    background: var(--page-bg);
  }
  .canvas {
    position: relative;
    width: 1200px;
    height: 902px;
  }
  .card {
    position: absolute;
    left: 100px;
    top: 166px;
    width: 1000px;
    height: 570px;
    background: var(--card-frost);
    box-shadow: 0 10px 30px rgba(0,0,0,0.18);
    overflow: hidden;
  }
  .card-shapes {
    position: absolute;
    inset: 0;
  }
  .holder {
    position: absolute;
    left: 48px;
    top: 104px;
    color: var(--text-gold);
  }
  .holder-name {
    font-family: "Cinzel", serif;
    font-weight: 400;
    font-size: 37px;
    letter-spacing: 1px;
    line-height: 1;
  }
  .holder-title {
    font-family: "Questrial", sans-serif;
    font-size: 24px;
    margin-top: 4px;
  }
  .contacts {
    position: absolute;
    left: 48px;
    top: 372px;
    list-style: none;
    font-family: "Questrial", sans-serif;
    font-size: 24px;
    color: var(--text-gold);
  }
  .contacts li {
    display: flex;
    align-items: center;
    height: 35px;
  }
  .contact-icon {
    width: 24px;
    height: 24px;
    margin-right: 12px;
    flex: none;
  }
  .brand {
    position: absolute;
    left: 520px;
    width: 480px;
    top: 352px;
    text-align: center;
    color: var(--logo-taupe);
  }
  .brand-name {
    font-family: "Cinzel", serif;
    font-size: 36px;
    line-height: 1;
    letter-spacing: 0.5px;
  }
  .brand-tagline {
    font-family: "Cinzel", serif;
    font-size: 16px;
    letter-spacing: 11px;
    margin-top: 6px;
  }
</style>
</head>
<body>
<main class="canvas">
  <section class="card" aria-label="Business card front">
    <svg class="card-shapes" viewBox="0 0 1000 570" width="1000" height="570" aria-hidden="true">
      <polygon points="0,0 356,0 559,570 0,570" fill="var(--panel-black)"/>
      <polygon points="356,0 417,0 567,570 559,570" fill="var(--accent-taupe)"/>
      <polygon points="417,0 422,0 572,570 567,570" fill="var(--panel-black)"/>
    </svg>

    <div class="holder">
      <h1 class="holder-name">ROWAN HALE</h1>
      <p class="holder-title">Chief Executive Officer</p>
    </div>

    <ul class="contacts">
      <li>
        <svg class="contact-icon" viewBox="0 0 24 24" aria-hidden="true">
          <rect width="24" height="24" fill="var(--accent-taupe)"/>
          <path d="M5 10 Q12 4 19 10 L17 12 L15 10 L9 10 L7 12 Z" fill="#000"/>
          <rect x="7" y="12" width="10" height="7" rx="1" fill="#000"/>
        </svg>
        <span>44 7900 318462</span>
      </li>
      <li>
        <svg class="contact-icon" viewBox="0 0 24 24" aria-hidden="true">
          <rect width="24" height="24" fill="var(--accent-taupe)"/>
          <rect x="4" y="6" width="16" height="12" fill="none" stroke="#000" stroke-width="1.6"/>
          <path d="M4 6 L12 13 L20 6 M4 18 L10 12 M20 18 L14 12" fill="none" stroke="#000" stroke-width="1.4"/>
        </svg>
        <span>hello@tavolenstudio.com</span>
      </li>
      <li>
        <svg class="contact-icon" viewBox="0 0 24 24" aria-hidden="true">
          <rect width="24" height="24" fill="var(--accent-taupe)"/>
          <circle cx="12" cy="12" r="8" fill="none" stroke="#000" stroke-width="1.5"/>
          <ellipse cx="12" cy="12" rx="3.5" ry="8" fill="none" stroke="#000" stroke-width="1.3"/>
          <path d="M4 12 H20 M5.5 8 H18.5 M5.5 16 H18.5" stroke="#000" stroke-width="1.2"/>
        </svg>
        <span>www.tavolenstudio.com</span>
      </li>
    </ul>

    <div class="brand">
      <p class="brand-name">Danvir Okelowa</p>
      <p class="brand-tagline">PHOTOGRAPHY</p>
    </div>
  </section>
</main>
</body>
</html>
```